Roving Beam Battles

Information can be taken and lifted from the professional website mobilelasertags.comI am a new start up in my area. I have no designs or logos of my own.The service we offer is Laser Tag using the Photon Dash brand. I would like their logo on my card. On the card I need my contact info, the different services we offer, with a focus on Law Enforcement / Military Training, Party, Celebration, Schools, Weekend and Holidays. I am open to any color and back grounds. It needs to have our rates listed as well as our service areas: Serving South Georgia Brantley, Camden, Charlton, Glynn, Pierce, Ware, McintoshServing North Florida Baker, Clay, Duval, Nassau, St. Johns, Union, Putnum, Flagler, AlachuaYou can find black and white images on the website.

Industry/Entity Type

It Professional

Contact Information for Business Card

Benjamin Hayward912-227-7195mobilelasertags.cominfo@rovingbeambattles.com

Requirements
Must have
• Service areas, rates, and events catered to.

```html
<!DOCTYPE html>
<html lang="en">
<head>
<meta charset="utf-8">
<title>Roving Beam Battles – Business Card</title>
<link rel="stylesheet" href="https://fonts.googleapis.com/css2?family=Noto+Serif:wght@400&family=Open+Sans:wght@400;600;800&display=swap">
<style>
  :root {
    --backdrop: #dcdcdc;
    --card-black: #000000;
    --brand-red: #c8202a;
    --rule-red: #d3222c;
    --panel-top: #c6c6c1;
    --panel-bottom: #b3a57f;
    --ink: #1a1a1a;
    --white: #ffffff;
  }
  * { margin: 0; padding: 0; box-sizing: border-box; }
  html, body {
    width: 992px; height: 1200px; overflow: hidden;
    background: var(--backdrop);
  }
  .canvas { position: relative; width: 992px; height: 1200px; }
  .card { position: absolute; left: 99px; width: 807px; overflow: hidden; }

  /* Front */
  .card--front { top: 103px; height: 462px; background: linear-gradient(to bottom, var(--panel-top) 0%, var(--panel-top) 45%, var(--panel-bottom) 100%); }
  .front-header {
    position: absolute; left: 0; top: 0; width: 100%; height: 255px;
    background: var(--card-black);
    border-bottom: 3px solid var(--rule-red);
    display: flex; align-items: center; justify-content: center; gap: 18px;
  }
  .brand-name {
    font-family: "Open Sans", sans-serif; font-weight: 800;
    font-size: 64px; color: var(--brand-red); letter-spacing: 1px;
  }
  .brand-dot { width: 58px; height: 58px; border-radius: 50%; background: var(--brand-red); }
  .owner-name {
    position: absolute; left: 46px; top: 340px;
    font-family: "Noto Serif", serif; font-weight: 400; font-size: 32px; line-height: 1;
    color: var(--brand-red);
  }
  .events {
    position: absolute; left: 46px; top: 390px; width: 320px;
    font-family: "Open Sans", sans-serif; font-size: 13px; line-height: 1.45;
    color: var(--ink);
  }
  .events strong { font-weight: 600; color: var(--brand-red); }
  .divider { position: absolute; left: 388px; top: 300px; width: 2px; height: 128px; background: var(--ink); }
  .contact { position: absolute; left: 423px; display: flex; align-items: center; gap: 24px; }
  .contact svg { width: 17px; height: 17px; flex: none; }
  .contact span { font-family: "Open Sans", sans-serif; font-size: 21px; line-height: 1; color: var(--ink); letter-spacing: 0.3px; }
  .contact--phone { top: 313px; }
  .contact--web { top: 352px; }
  .contact--mail { top: 392px; }

  /* Back */
  .card--back { top: 624px; height: 461px; background: var(--card-black); }
  .area-heading {
    position: absolute; left: 64px;
    font-family: "Noto Serif", serif; font-weight: 400; line-height: 1; color: var(--brand-red);
  }
  .area-heading--georgia { top: 47px; font-size: 30px; }
  .area-heading--florida { top: 253px; font-size: 32px; }
  .county {
    position: absolute; font-family: "Open Sans", sans-serif;
    font-size: 25px; line-height: 1; color: var(--white); letter-spacing: 0.4px;
  }
  .rates { position: absolute; left: 291px; top: 150px; width: 240px; }
  .rates-heading {
    font-family: "Noto Serif", serif; font-weight: 400; font-size: 20px; line-height: 1;
    color: var(--brand-red); margin-bottom: 8px;
  }
  .rates-text {
    font-family: "Open Sans", sans-serif; font-size: 15px; line-height: 1.4; color: var(--white);
  }
</style>
</head>
<body>
<div class="canvas">

  <section class="card card--front">
    <header class="front-header">
      <span class="brand-name">Photon Dash</span>
      <span class="brand-dot"></span>
    </header>

    <p class="owner-name">Gordon Whitlock</p>
    <p class="events"><strong>Events:</strong> Law Enforcement / Military Training · Parties · Celebrations · Schools · Weekends &amp; Holidays</p>
    <div class="divider"></div>

    <div class="contact contact--phone">
      <svg viewBox="0 0 16 16" aria-hidden="true"><rect width="16" height="16" fill="var(--brand-red)"/><path d="M5 3.5l2 2-1 1.2c.6 1.3 1.7 2.4 3 3l1.2-1 2 2-1.3 1.6C7.5 12 4 8.5 3.7 4.8z" fill="var(--white)"/></svg>
      <span>912-555-0148</span>
    </div>
    <div class="contact contact--web">
      <svg viewBox="0 0 16 16" aria-hidden="true"><rect width="16" height="16" fill="var(--brand-red)"/><circle cx="8" cy="8" r="4.5" fill="none" stroke="var(--white)" stroke-width="1.3"/><path d="M3.5 8h9M8 3.5c-2 2.5-2 6.5 0 9M8 3.5c2 2.5 2 6.5 0 9" fill="none" stroke="var(--white)" stroke-width="1"/></svg>
      <span>www.rovingbeambattles.com</span>
    </div>
    <div class="contact contact--mail">
      <svg viewBox="0 0 16 16" aria-hidden="true"><rect width="16" height="16" fill="var(--brand-red)"/><rect x="3" y="4.5" width="10" height="7" fill="var(--white)"/><path d="M3 4.5l5 4 5-4" fill="none" stroke="var(--brand-red)" stroke-width="1"/></svg>
      <span>info@rovingbeambattles.com</span>
    </div>
  </section>

  <section class="card card--back">
    <h2 class="area-heading area-heading--georgia">SERVICE AREAS:</h2>
    <span class="county" style="left:99px; top:104px;">Brantley</span>
    <span class="county" style="left:99px; top:150px;">Charlton</span>
    <span class="county" style="left:99px; top:201px;">Camden</span>
    <span class="county" style="left:291px; top:104px;">McIntosh</span>
    <span class="county" style="left:561px; top:106px;">Ware</span>
    <span class="county" style="left:561px; top:152px;">Glynn</span>
    <span class="county" style="left:561px; top:201px;">Pierce</span>

    <div class="rates">
      <h3 class="rates-heading">RATES:</h3>
      <p class="rates-text">Hourly &amp; event packages<br>Call for a free quote</p>
    </div>

    <h2 class="area-heading area-heading--florida">Serving North Florida:</h2>
    <span class="county" style="left:99px; top:313px;">Baker</span>
    <span class="county" style="left:99px; top:351px;">Clay</span>
    <span class="county" style="left:99px; top:391px;">Duval</span>
    <span class="county" style="left:291px; top:313px;">St. Johns</span>
    <span class="county" style="left:291px; top:351px;">Union</span>
    <span class="county" style="left:291px; top:391px;">Putnum</span>
    <span class="county" style="left:559px; top:311px;">Flagler</span>
    <span class="county" style="left:559px; top:351px;">Nassau</span>
    <span class="county" style="left:559px; top:391px;">Alachua</span>
  </section>

</div>
</body>
</html>
```